Stationery Design Project

We need a stationery design for our Norwegian trucking company. We have existed for about 15 years and our 12 drivers uses relatively new vehicles to transport goods around in northern Norway. Long distance routes with fresh fish og food transport is our main operations.

We have already made alogo that's printed on our trucks. The logo and a picture of our trucks is attached. I think the logo i crappy, but since its already in use, changing it is not an option in this round. Still using a better colour scheme in the overall stationery and more interesting fonts is possible (altso in the logo).

Company details:
Name: Vikstrandbil AS
Organisation nr 981 537 608
Post adress: 8613 Lysvær

I like minimalism and simplicity. I am avalibly for questions in normal GMT working hours either here or on mail: petter@vikstrand.no

Reason: Hi. Im extending the deadline because I needed some time to find a vector file of our logo. Sorry for the inconvenience

Hi, and thanks for all your interest in the project. Some updates:

-          I have decided to commit to using one of the designs. Some designer will get the payment.

-          I have extended the deadline with 24 hours since I needed some time to find our firms vector logo (a slow Swedish man was holding me up)

-          We will not choose a design before the deadline. No need to rush.

-          We have received a lot of great design and think there is a need to specified the product we want to make:

o   Business Card for all our employers. I just need the design and will duplicate with the correct numbers and name myself. The information on should be: Logo, employer’s name, Phone number, email, website, Postal number and address. Use this as a template: logo, Leif Brattli, 47283916, Leif@vikstrand.no,, vikstrand.no, 8613 Lysvær. The order and placement of the information is your creative decision.

o   Stickers to put on the goods we travel. On the sticker the should be the following information: Logo, phone number, Tekst and link: Fraktæ av Vikstrandbil. Ke du syns? Vikstrand.no/tilbakemelding (this means: Handled by Vikstrandbil. What do you think Vikstrand.no/feedback -à the link will be a feedback form). The placement the information and size is your creative decision with some stings: we have been thinking of using Prentavo for printing and see that a size about 6x6 cm, 8x5 or something like that. (with 3000 copies our budget is 200 punds). Any suggestions of other suppliers are welcome. Prentavo price calculator http://www.prentavoprint.co.uk/digital-litho-printing/printing-labels-tags/stickers/

o   Letterhead with logo, address, phone number and organizational number.

o   Envelopes with logo,address, phone number and organizational number.

Have a nice day.

 

 

• Using the blue colour in the logo and using a similar graphic approch.

```html
<!DOCTYPE html>
<html lang="no">
<head>
<meta charset="utf-8">
<title>Vikstrandbil – fraktetikett</title>
<link rel="stylesheet" href="https://fonts.googleapis.com/css2?family=Saira:wght@400;600&display=swap">
<style>
  :root {
    --page-bg: #ececec;
    --brand-blue: #1677d2;
    --brand-navy: #052f86;
    --brand-ink: #0a3a96;
    --paper: #ffffff;
    --text-dark: #2b2b2b;
  }
  * { margin: 0; padding: 0; box-sizing: border-box; }
  html, body { width: 1200px; height: 900px; overflow: hidden; }
  body {
    background: var(--page-bg);
    font-family: "Saira", "Arial", sans-serif;
    position: relative;
  }
  .sticker {
    position: absolute;
    left: 268px; top: 242px;
    width: 663px; height: 415px;
    overflow: hidden;
    background: var(--paper);
  }
  .sticker-frame { position: absolute; inset: 0; }
  .sticker-content {
    position: absolute; inset: 0;
    text-align: center;
    color: var(--text-dark);
  }
  .brand-name {
    position: absolute; left: 0; right: 0; top: 64px;
    display: flex; justify-content: center; align-items: center; gap: 14px;
    font-size: 50px; font-weight: 600; line-height: 1;
    color: var(--brand-ink);
  }
  .brand-dot {
    width: 22px; height: 22px; border-radius: 50%;
    background: var(--brand-blue);
  }
  .handled-by {
    position: absolute; left: 0; right: 0; top: 194px;
    font-size: 30px; font-weight: 400; line-height: 1;
  }
  .question {
    position: absolute; left: 0; right: 0; top: 235px;
    font-size: 37px; font-weight: 400; line-height: 1;
  }
  .feedback-link {
    position: absolute; left: 0; right: 0; top: 278px;
    font-size: 38px; font-weight: 400; line-height: 1;
    color: var(--brand-ink);
  }
  .phone {
    position: absolute; left: 0; right: 0; top: 362px;
    display: flex; justify-content: center; align-items: center; gap: 18px;
    font-size: 26px; line-height: 1;
  }
  .phone-icon { width: 22px; height: 22px; }
</style>
</head>
<body>
  <div class="sticker">
    <svg class="sticker-frame" width="663" height="415" viewBox="0 0 663 415" aria-hidden="true">
      <rect width="663" height="415" fill="var(--brand-blue)"/>
      <path d="M470 0 H663 V150 Z" fill="var(--brand-navy)"/>
      <path d="M0 300 L0 415 H200 Z" fill="var(--brand-navy)"/>
      <path d="M585 45 Q640 85 663 125 L663 108 Q625 70 585 45 Z" fill="var(--paper)"/>
      <path d="M0 325 Q40 350 72 370 Q35 345 0 340 Z" fill="var(--paper)"/>
      <ellipse cx="331" cy="207" rx="360" ry="260" fill="var(--paper)"/>
    </svg>
    <div class="sticker-content">
      <div class="brand-name"><span class="brand-dot"></span>Vikstrandbil</div>
      <p class="handled-by">Fraktæ av Vikstrandbil.</p>
      <p class="question">KE DU SYNS?</p>
      <p class="feedback-link">Vikstrand.no/tilbakemelding</p>
      <p class="phone">
        <svg class="phone-icon" viewBox="0 0 22 22" aria-label="Telefon" role="img">
          <rect x="1" y="2" width="20" height="18" rx="1.5" fill="none" stroke="var(--brand-navy)" stroke-width="2"/>
          <rect x="4" y="5" width="4" height="12" fill="var(--brand-navy)"/>
          <g fill="var(--brand-navy)">
            <rect x="10" y="5" width="2.5" height="2.5"/><rect x="14.5" y="5" width="2.5" height="2.5"/>
            <rect x="10" y="9.5" width="2.5" height="2.5"/><rect x="14.5" y="9.5" width="2.5" height="2.5"/>
            <rect x="10" y="14" width="2.5" height="2.5"/><rect x="14.5" y="14" width="2.5" height="2.5"/>
          </g>
        </svg>
        <span>981 537 608</span>
      </p>
    </div>
  </div>
</body>
</html>
```